Sunlit Path Society the biggest community for CarbonOffset in the travel industry

We are a platform building a community for people to be able to measure and compensate carbon footprint. This community will be focused on Individuals and Businesses where they can measure their impact and choose projects to offset. I want to have a calculator of the number of kms being compensated as a community as well as the number of tons being removed. We are building the biggest community in the travel industry where users of Tours, Car Rentals, Events and eventually hotels will measure their footprint and contribute to a project to compensate and become part of the community to learn, connect and help with the environment. We will also invite companies to be part of the project so that they can offer this to their clients and employees.

Target Market(s)

At first travelers on holidays, business, events, conferences, tour operators. Next phase rental car companies, ride sharing apps

Industry/Entity Type

Travel

Number of Pages Required

1 page

Font styles to use
Serif
Sans Serif

Colors

Designer to choose colors to be used in the design.

Requirements
Must have
• A lot of images with an optimist focus. I want to stop the message that we are doomed and change it to we have an opportunity to do something, celebrate about that and build a community around this. It is intended for people between 25 - 50 years old. I want this project to be more human, our interaction and need to connect with nature. How it benefits us, etc.
Nice to have
• Videos of the projects, videos of people from the community sharing their thoughts. I am imagining somewhere within the webpage to have a mosaic with the pictures (from facebook if authorised by each person) to get and idea of how big the community is and put a human face.
Should not have
• Blaming messages of how the world will end, we have enough information on that.

```html
<!DOCTYPE html>
<html lang="en">
<head>
<meta charset="utf-8">
<title>Sunlit Path Society</title>
<link href="https://fonts.googleapis.com/css2?family=Barlow:ital,wght@0,400;0,500;0,600;0,700;1,500&display=swap" rel="stylesheet">
<style>
:root{
  --blue:#0a47a0;
  --blue-mid:#1565c8;
  --green:#3fae3a;
  --ink:#1d1d1d;
  --text:#555b63;
  --grey-band:#efefef;
  --pale-blue:#e6edf7;
  --footer:#f3f3f3;
  --white:#fff;
}
*{box-sizing:border-box;margin:0;padding:0}
html,body{width:1200px;height:4505px;overflow:hidden}
body{font-family:"Barlow",sans-serif;color:var(--ink);background:var(--white);position:relative}
.abs{position:absolute}
.rule{width:62px;height:3px;background:var(--blue);margin:0 auto}
.pill{display:inline-block;border:2px solid var(--blue);color:var(--blue);border-radius:20px;font-weight:600;font-size:13px;padding:6px 16px;letter-spacing:.3px}

.site-header{left:0;top:0;width:1200px;height:93px;background:var(--white)}
.brand{left:143px;top:15px;font-weight:700;font-size:27px;line-height:31px;color:var(--ink)}
.nav{right:145px;top:38px;display:flex;gap:24px;font-size:15px;font-weight:500}
.nav .active{color:var(--green)}

.hero{left:0;top:93px;width:1200px;height:638px;background:linear-gradient(180deg,#2f9a3a 0%,#46b24a 45%,#6cc25a 75%,#3c8b3a 100%)}
.hero h1{position:absolute;top:120px;width:100%;text-align:center;color:var(--white);font-size:48px;font-weight:700}
.hero p{position:absolute;top:186px;width:100%;text-align:center;color:var(--white);font-size:18px;line-height:31px}
.hero-btns{position:absolute;top:272px;width:100%;display:flex;justify-content:center;gap:20px}
.hero-btns span{font-size:13px;font-weight:600;color:var(--white);padding:10px 20px;border:2px solid var(--white)}
.hero-btns .fill{background:var(--green);border-color:var(--green)}
.hero-dots{position:absolute;top:352px;width:100%;display:flex;justify-content:center;gap:12px}
.hero-dots i{width:17px;height:17px;border-radius:50%;border:2px solid var(--white)}
.hero-dots i.on{background:var(--blue-mid);border-color:#7fb5f0}

.features{left:143px;top:668px;width:912px;height:355px;background:var(--white);box-shadow:0 6px 22px rgba(0,0,0,.14);display:flex}
.feature{flex:1;text-align:center;padding-top:28px;border-right:1px solid #ececec}
.feature:last-child{border:0}
.feature .icon{width:102px;height:102px;border-radius:50%;margin:0 auto;background:radial-gradient(circle at 35% 30%,#2b7fe0,#0a47a0 70%);display:flex;align-items:center;justify-content:center}
.feature h3{font-size:19px;font-weight:500;margin-top:18px}
.feature p{font-size:13px;line-height:24px;color:var(--text);padding:8px 12px 12px;height:116px}

.about{left:0;top:1100px;width:1200px;text-align:center}
.about h2{font-size:37px;font-weight:400;margin-bottom:18px}
.about h2 b{font-weight:700}
.about p{width:760px;margin:30px auto 0;font-size:14.5px;line-height:30.5px;color:var(--text)}
.about .pill{margin-top:30px;font-size:15px;padding:8px 24px}

.services{left:0;top:1518px;width:1200px;height:700px;background:var(--grey-band)}
.services h2,.creds h2,.care h2{text-align:center;font-size:37px;font-weight:700;margin-bottom:20px}
.services h2{margin-top:80px}
.svc{position:absolute;top:219px;width:288px;height:393px}
.svc .photo{height:248px}
.svc .edge{position:absolute;left:14px;top:168px}
.svc .panel{position:absolute;left:14px;right:14px;top:188px;bottom:0;background:var(--white);box-shadow:0 6px 14px rgba(0,0,0,.1);text-align:center;padding:10px 16px 0}
.svc h3{font-size:18px;font-weight:500}
.svc p{font-size:13px;line-height:22px;color:var(--text);margin-top:12px}
.svc .tag{position:absolute;right:0;bottom:0;background:var(--blue);color:var(--white);font-size:12px;font-weight:600;padding:9px 16px 9px 26px;clip-path:polygon(12px 0,100% 0,100% 100%,0 100%)}

.testimonials{left:0;top:2169px;width:1200px;height:708px;background:linear-gradient(180deg,#0b4aa3,#0a3f92)}
.testimonials h2{position:absolute;top:182px;width:100%;text-align:center;color:var(--white);font-size:37px;font-weight:700}
.testimonials .rule{position:absolute;top:257px;left:569px;background:var(--white)}
.quote{position:absolute;width:295px;border:2px solid rgba(255,255,255,.85);text-align:center;color:var(--white);padding:70px 20px 0}
.quote .avatar{position:absolute;left:50%;top:-48px;margin-left:-48px;width:96px;height:96px;border-radius:50%;border:3px solid var(--white);background:radial-gradient(circle,#c9d6e8,#6d86aa)}
.quote p{font-size:13.5px;line-height:24px}
.quote em{display:block;margin-top:14px;font-size:13.5px;font-weight:500}
.t-dots{position:absolute;top:2803px;left:0;width:1200px;display:flex;justify-content:center;gap:8px}
.t-dots i{width:15px;height:15px;border-radius:50%;border:2px solid var(--white)}
.t-dots i.on{background:var(--white)}

.creds{left:0;top:2877px;width:1200px;height:385px;background:var(--pale-blue)}
.creds h2{margin-top:72px}
.badges{position:absolute;top:196px;left:143px;display:flex;gap:18px}
.badge{width:214px;height:93px;background:var(--white);display:flex;align-items:center;justify-content:center}
.badge i{display:block;width:130px;height:36px;background:#c4cbd4;border-radius:4px}

.care{left:0;top:3262px;width:1200px;height:752px}
.care h2{margin-top:72px}
.post{position:absolute;top:201px;width:285px;height:434px;background:var(--white);box-shadow:0 4px 14px rgba(0,0,0,.1)}
.post.alt{background:#e8eef8;border-left:3px solid var(--blue)}
.post .photo{height:183px}
.post .body{padding:20px 21px}
.post .date{color:var(--blue);font-style:italic;font-weight:500;font-size:13px;display:flex;align-items:center;gap:6px}
.post h3{color:var(--blue);font-weight:500;font-size:18px;line-height:24px;margin-top:14px}
.post p{font-size:13px;line-height:24px;color:var(--text);margin-top:14px}
.post .pill{margin-top:14px;font-size:12px;padding:5px 20px}

.site-footer{left:0;top:4014px;width:1200px;height:367px;background:var(--footer)}
.f-brand{position:absolute;left:143px;top:76px;font-size:27px;font-weight:700;line-height:31px}
.socials{position:absolute;left:143px;top:148px;display:flex;gap:6px}
.socials i{width:29px;height:29px;border-radius:50%;border:1.5px solid #333}
.f-col{position:absolute;top:80px}
.f-col h4{font-size:18px;font-weight:500;margin-bottom:24px}
.f-col p,.f-col li{font-size:13px;line-height:21px;color:#333}
.field{width:272px;height:38px;border:1px solid #ccc;border-radius:20px;background:var(--white);margin-top:18px;font-size:11px;color:#777;padding:11px 14px}
.subscribe{display:inline-block;margin-top:20px;background:var(--green);color:var(--white);font-size:13px;font-weight:600;padding:9px 22px;border-radius:20px}
.contact-row{display:flex;gap:14px;margin-bottom:14px}
.contact-row svg{flex:none;margin-top:3px}
.links{list-style:none}
.links li{line-height:27.5px}
.copyright{left:0;top:4431px;width:1200px;text-align:center;font-size:13px;color:#333}
</style>
</head>
<body>

<header class="site-header abs">
  <div class="brand abs">SUNLIT PATH<br>SOCIETY</div>
  <nav class="nav abs">
    <span class="active">HOME</span><span>SERVICES</span><span>CALCULATE</span><span>OFFSETTING</span><span>ABOUT</span><span>BLOG</span><span>CONTACT</span>
  </nav>
</header>

<section class="hero abs" role="img" aria-label="Paper-cut illustration of green trees, clouds, a wind turbine and a white city skyline on a green background">
  <h1>SUNLIT PATH SOCIETY</h1>
  <p>Measure and offset the footprint of every tour, car rental and event,<br>and join the biggest travel community celebrating greener journeys</p>
  <div class="hero-btns"><span>REQUEST A DEMO</span><span class="fill">LEARN MORE</span></div>
  <div class="hero-dots"><i class="on"></i><i></i><i></i></div>
</section>

<section class="features abs">
  <div class="feature">
    <div class="icon"><svg width="54" height="50" viewBox="0 0 54 50" fill="none" stroke="#fff" stroke-width="2.5"><rect x="6" y="30" width="7" height="16"/><rect x="19" y="24" width="7" height="22"/><rect x="32" y="18" width="7" height="28"/><path d="M4 22 L16 12 L28 16 L46 4"/><circle cx="46" cy="4" r="3"/></svg></div>
    <h3>Calculate</h3>
    <p>Together our community has compensated 1,284,500 km of travel and removed 312 tons of CO₂ so far</p>
    <span class="pill">READ MORE</span>
  </div>
  <div class="feature">
    <div class="icon"><svg width="52" height="48" viewBox="0 0 52 48" fill="none" stroke="#fff" stroke-width="2.5"><path d="M4 4 V44 H48"/><rect x="12" y="14" width="7" height="24"/><rect x="24" y="22" width="7" height="16"/><rect x="36" y="28" width="7" height="10"/></svg></div>
    <h3>Reduce</h3>
    <p>Simple choices on tours, car rentals and events that lower the impact of every trip you take</p>
    <span class="pill">READ MORE</span>
  </div>
  <div class="feature">
    <div class="icon"><svg width="54" height="54" viewBox="0 0 54 54" fill="none" stroke="#fff" stroke-width="2.5"><path d="M27 36 V14"/><path d="M27 22 C20 22 16 16 16 12 C22 12 27 16 27 22"/><path d="M27 18 C34 18 38 12 38 8 C32 8 27 12 27 18"/><path d="M6 42 H18 L28 46 L46 38"/><path d="M6 48 H44"/></svg></div>
    <h3>Offset</h3>
    <p>Choose the nature projects you love and compensate your journey with travellers worldwide</p>
    <span class="pill">READ MORE</span>
  </div>
  <div class="feature">
    <div class="icon"><svg width="56" height="52" viewBox="0 0 56 52" fill="none" stroke="#fff" stroke-width="2.5"><path d="M8 28 L30 18 V46 L8 36 Z"/><path d="M30 22 H40 V42 H30"/><circle cx="42" cy="10" r="6"/><circle cx="20" cy="8" r="4"/><path d="M46 28 H52 M46 34 L51 38"/></svg></div>
    <h3>Communicate</h3>
    <p>Share your story, connect with fellow travellers and celebrate every step we take together</p>
    <span class="pill">READ MORE</span>
  </div>
</section>

<section class="about abs">
  <h2>About <b>Sunlit Path Society</b></h2>
  <div class="rule"></div>
  <p>We are building the biggest community in the travel industry for people who love to explore and want to give back to nature. Travellers on holidays, business trips, events and conferences can measure the footprint of their tours, car rentals and events, then choose a project to compensate it. Companies and tour operators can join too and offer offsetting to their clients and employees. This is not about blame, it is an opportunity to learn, connect and celebrate the difference we make together</p>
  <span class="pill">READ MORE</span>
</section>

<section class="services abs">
  <h2>Our Services</h2>
  <div class="rule"></div>
  <article class="svc" style="left:128px">
    <div class="photo" role="img" aria-label="Laptop on a desk with a small plant on screen" style="background:linear-gradient(160deg,#4a5a48,#1e2620)"></div>
    <svg class="edge" width="260" height="22" viewBox="0 0 260 22"><polygon points="0,22 260,0 260,22" fill="#fff"/><line x1="0" y1="21" x2="260" y2="1" stroke="#1565c8" stroke-width="3"/></svg>
    <div class="panel"><h3>Setting up &amp; Managing</h3><p>We help tour operators and event hosts set up offsetting for their travellers and manage it with ease</p><span class="tag">LEARN MORE</span></div>
  </article>
  <article class="svc" style="left:455px">
    <div class="photo" role="img" aria-label="Team gathered around a table drawing growth charts on paper" style="background:linear-gradient(160deg,#b9a592,#e9e7e2)"></div>
    <svg class="edge" width="260" height="22" viewBox="0 0 260 22"><polygon points="0,22 260,0 260,22" fill="#fff"/><line x1="0" y1="21" x2="260" y2="1" stroke="#1565c8" stroke-width="3"/></svg>
    <div class="panel"><h3>Carbon Neutrality</h3><p>Make conferences, rentals and business trips carbon neutral and share the result with your team</p><span class="tag">LEARN MORE</span></div>
  </article>
  <article class="svc" style="left:782px">
    <div class="photo" role="img" aria-label="Hands working over papers and a laptop on a wooden desk" style="background:linear-gradient(160deg,#6b5a4a,#2a211b)"></div>
    <svg class="edge" width="260" height="22" viewBox="0 0 260 22"><polygon points="0,22 260,0 260,22" fill="#fff"/><line x1="0" y1="21" x2="260" y2="1" stroke="#1565c8" stroke-width="3"/></svg>
    <div class="panel"><h3>Measure and Compensate</h3><p>Calculate the kilometres of each journey and compensate them through projects you choose</p><span class="tag">LEARN MORE</span></div>
  </article>
</section>

<section class="testimonials abs">
  <svg class="abs" style="left:0;top:0" width="1200" height="60" viewBox="0 0 1200 60" preserveAspectRatio="none"><path d="M0 0 H1200 V26 C900 -10 300 -10 0 26 Z" fill="#efefef"/></svg>
  <h2>Client Testimonials</h2>
  <div class="rule"></div>
  <div class="quote" style="left:143px;top:387px;height:217px"><div class="avatar" role="img" aria-label="Client portrait"></div><p>Sed ut perspiciatis unde omnis iste natus error sit voluptatem accusantium doloremque laudantium, totam rem aperiam, eaque ipsa quae ab</p><em>Nemo enim ipsam</em></div>
  <div class="quote" style="left:452px;top:371px;height:217px"><div class="avatar" role="img" aria-label="Client portrait"></div><p>Sed ut perspiciatis unde omnis iste natus error sit voluptatem accusantium doloremque laudantium, totam rem aperiam, eaque ipsa quae ab</p><em>Nemo enim ipsam</em></div>
  <div class="quote" style="left:760px;top:387px;height:217px"><div class="avatar" role="img" aria-label="Client portrait"></div><p>Sed ut perspiciatis unde omnis iste natus error sit voluptatem accusantium doloremque laudantium, totam rem aperiam, eaque ipsa quae ab</p><em>Nemo enim ipsam</em></div>
</section>
<div class="t-dots"><i class="on"></i><i></i><i></i></div>

<section class="creds abs">
  <h2>Our Credentials</h2>
  <div class="rule"></div>
  <div class="badges">
    <div class="badge" role="img" aria-label="Partner badge"><i></i></div>
    <div class="badge" role="img" aria-label="Certification badge"><i></i></div>
    <div class="badge" role="img" aria-label="Membership badge"><i></i></div>
    <div class="badge" role="img" aria-label="Accreditation badge"><i></i></div>
  </div>
</section>

<section class="care abs">
  <h2>Sustainability &amp; Community Care</h2>
  <div class="rule"></div>
  <article class="post" style="left:143px">
    <div class="photo" role="img" aria-label="Hand touching a green CO2 symbol on a digital screen" style="background:linear-gradient(135deg,#3a4a66,#6e89a8)"></div>
    <div class="body"><div class="date"><svg width="12" height="12" viewBox="0 0 12 12"><rect x="1" y="2" width="10" height="9" fill="none" stroke="#0a47a0" stroke-width="1.4"/><path d="M1 5 H11" stroke="#0a47a0" stroke-width="1.4"/></svg>October 17, 2019</div><h3>Nemo enim ipsam voluptatem quia voluptas sit</h3><p>Sed ut perspiciatis unde omnis iste natus error sit voluptatem accusantium doloremque laudantium, totam rem</p><span class="pill">READ MORE</span></div>
  </article>
  <article class="post alt" style="left:456px">
    <div class="photo" role="img" aria-label="Green growth arrow rising over a city skyline" style="background:linear-gradient(180deg,#d9dde0,#8a9488)"></div>
    <div class="body"><div class="date"><svg width="12" height="12" viewBox="0 0 12 12"><rect x="1" y="2" width="10" height="9" fill="none" stroke="#0a47a0" stroke-width="1.4"/><path d="M1 5 H11" stroke="#0a47a0" stroke-width="1.4"/></svg>October 17, 2019</div><h3>Nemo enim ipsam voluptatem quia voluptas sit</h3><p>Sed ut perspiciatis unde omnis iste natus error sit voluptatem accusantium doloremque laudantium, totam rem</p><span class="pill">READ MORE</span></div>
  </article>
  <article class="post" style="left:770px">
    <div class="photo" role="img" aria-label="Tablet showing charts on a desk with a coffee cup" style="background:linear-gradient(135deg,#e4e9ef,#8aa4c4)"></div>
    <div class="body"><div class="date"><svg width="12" height="12" viewBox="0 0 12 12"><rect x="1" y="2" width="10" height="9" fill="none" stroke="#0a47a0" stroke-width="1.4"/><path d="M1 5 H11" stroke="#0a47a0" stroke-width="1.4"/></svg>October 17, 2019</div><h3>Nemo enim ipsam voluptatem quia voluptas sit</h3><p>Sed ut perspiciatis unde omnis iste natus error sit voluptatem accusantium doloremque laudantium, totam rem</p><span class="pill">READ MORE</span></div>
  </article>
</section>

<footer class="site-footer abs">
  <div class="f-brand">SUNLIT PATH<br>SOCIETY</div>
  <div class="socials"><i></i><i></i><i></i><i></i></div>
  <div class="f-col" style="left:350px">
    <h4>SIGN UP FOR NEWSLETTER</h4>
    <p>Excepteur sint occaecat cupidatat non<br>proident, sunt in culpa qui officia deserunt</p>
    <div class="field">Enter email</div>
    <span class="subscribe">SUBSCRIBE</span>
  </div>
  <div class="f-col" style="left:663px">
    <h4>CONTACT US</h4>
    <div class="contact-row"><svg width="14" height="18" viewBox="0 0 14 18"><path d="M7 17 C3 11 1 8 1 6 A6 6 0 0 1 13 6 C13 8 11 11 7 17 Z" fill="#3fae3a"/><circle cx="7" cy="6" r="2.2" fill="#f3f3f3"/></svg><p>Sunlit Path Society<br>48 Meadow Lane,<br>Harbor Town HT2-0400</p></div>
    <div class="contact-row"><svg width="16" height="16" viewBox="0 0 16 16"><path d="M3 1 L6 4 L4.5 6 C5.5 8.5 7.5 10.5 10 11.5 L12 10 L15 13 L13 15 C7 15 1 9 1 3 Z" fill="#3fae3a"/></svg><p>Phone:<br>1300-555-014</p></div>
    <div class="contact-row"><svg width="16" height="14" viewBox="0 0 16 14"><rect x="1" y="2" width="14" height="10" fill="#3fae3a"/><path d="M1 2 L8 8 L15 2" fill="none" stroke="#f3f3f3" stroke-width="1.3"/></svg><p>Email:<br>info@sunlitpathsociety.com</p></div>
  </div>
  <div class="f-col" style="left:946px">
    <h4>QUICK LINKS</h4>
    <ul class="links"><li>Home</li><li>Services</li><li>Calculate</li><li>Offsetting</li><li>About</li><li>Blog</li><li>Contact</li></ul>
  </div>
</footer>

<div class="copyright abs">Sunlit Path Society © 2019 All Rights Reserved | Privacy Policy | Terms and Conditions</div>

</body>
</html>
```